Full Service Outdoor Property Management Company

We are looking for a new and fresh business card design. My company has been in business for 26 years. Winter: We are a large snow and ice management company that does work for commercial, industrial and municipal clients. We have been named "Top 100 Snow Companies in the U.S." for numerous years. Summer: We provide complete landscape maintenance and landscape design and construction for both residential and commercial clients. We must incorporate our logo into card design as well as (in no particular order):
Employees name
Office: (417) 803-2765
Cell: (xxx) xxx-xxxx
brightfold.com
1879 Marigold, Larkmoor WI 53208
(Something about 26 + years in business as well as "Top 100 snow contractors as stated above)
Target Market(s)
Winter: Commercial, Industrial, Municipal
Summer: Residential and Commercial
Industry/Entity Type
Construction
Contact Information for Business Card
This is a little challenging as we are using one card for essentially two companies that target different customers from summer to winter. Perhaps the back side could be split in two or something to highlight the different services?? I'm open to any ideas!! Looking forward to seeing what you come up with!
Requirements
Must have
- Logo
- (in no particular order)
- Employees name
- Office: (417) 803-2765
- Cell: (xxx) xxx-xxxx
- brightfold.com
- 1879 Marigold, Larkmoor WI 53208
Nice to have
- Something about 26 + years in business
- "Trusted Snow & Lawn Care Since 1998"
Should not have
- Cheesy pictures of lawn mowers and snow plows

```html
<!DOCTYPE html>
<html lang="en">
<head>
<meta charset="utf-8">
<title>Brightfold Business Card</title>
<link href="https://fonts.googleapis.com/css2?family=Roboto:wght@300;400&display=swap" rel="stylesheet">
<style>
  :root {
    --bg: #e9e6e1;
    --paper: #ffffff;
    --ink: #000000;
    --green: #138a43;
    --blue: #1a7bc8;
    --white: #ffffff;
  }
  * { margin: 0; padding: 0; box-sizing: border-box; }
  html, body { width: 1200px; height: 848px; overflow: hidden; }
  body {
    background: var(--bg);
    font-family: "Roboto", Arial, sans-serif;
    display: flex;
    align-items: center;
    justify-content: center;
    gap: 40px;
  }
  .card {
    position: relative;
    width: 540px;
    height: 309px;
    background: var(--paper);
    overflow: hidden;
    box-shadow: 0 6px 18px rgba(0,0,0,0.18);
  }
  .card-curve { position: absolute; inset: 0; }
  .brand-name {
    position: absolute;
    color: var(--green);
    font-weight: 400;
    letter-spacing: 0.5px;
  }
  .front .brand-name { left: 34px; top: 66px; font-size: 44px; }
  .employee-name {
    position: absolute;
    right: 22px; top: 14px;
    color: var(--green);
    font-weight: 300;
    font-size: 17px;
  }
  .contact-list {
    position: absolute;
    right: 22px; top: 118px;
    list-style: none;
    color: var(--white);
    font-weight: 300;
    font-size: 15px;
    line-height: 24px;
    text-align: right;
  }
  .contact-list li { display: flex; justify-content: flex-end; align-items: center; gap: 10px; }
  .contact-list .address { font-size: 16px; }
  .contact-list svg { width: 11px; height: 11px; fill: var(--white); flex: none; }
  .tagline {
    position: absolute;
    right: 22px; bottom: 22px;
    color: var(--white);
    font-weight: 300;
    font-size: 19px;
    white-space: nowrap;
  }
  .back .brand-name {
    left: 0; right: 0; top: 96px;
    text-align: center;
    font-size: 64px;
  }
  .stripes { position: absolute; left: 0; right: 0; bottom: 14px; }
  .stripe { height: 5px; margin-top: 7px; }
  .stripe.green { background: var(--green); }
  .stripe.blue { background: var(--blue); }
  .stripe.black { background: var(--ink); }
</style>
</head>
<body>
  <section class="card front">
    <svg class="card-curve" viewBox="0 0 540 309" preserveAspectRatio="none" aria-hidden="true">
      <path d="M540 30 C330 60 150 160 70 309 L540 309 Z" fill="var(--ink)"/>
    </svg>
    <div class="brand-name">Brightfold</div>
    <div class="employee-name">Employees name</div>
    <ul class="contact-list">
      <li>(417) 803-2765
        <svg viewBox="0 0 12 12"><path d="M2 1h3l1 3-2 1a7 7 0 0 0 3 3l1-2 3 1v3c-6 0-9-3-9-9z"/></svg></li>
      <li>(xxx) xxx-xxxx
        <svg viewBox="0 0 12 12"><path d="M3 0h6v12H3zM4 1v8h4V1z"/></svg></li>
      <li>brightfold.com
        <svg viewBox="0 0 12 12"><circle cx="6" cy="6" r="6"/></svg></li>
      <li class="address">1879 Marigold, Larkmoor WI 53208
        <svg viewBox="0 0 12 12"><path d="M6 0a4 4 0 0 1 4 4c0 3-4 8-4 8S2 7 2 4a4 4 0 0 1 4-4z"/></svg></li>
    </ul>
    <div class="tagline">"Trusted Snow &amp; Lawn Care Since 1998"</div>
  </section>

  <section class="card back">
    <div class="brand-name">Brightfold</div>
    <div class="stripes">
      <div class="stripe green"></div>
      <div class="stripe blue"></div>
      <div class="stripe black"></div>
    </div>
  </section>
</body>
</html>
```